Website Needs Designing / Populating

We are a Business Consultancy in London. We are Headhunters and Recruitment. I have bought the Domain, and Wordpress Site, installed a template from Layout Heron. I have tried to do it myself but do not have the time to complete or do it as I want / need.
I have some 'stock' pics and a logo - see uploaded logo files.
I want an easy to use Website - tells clients and viewers what we are about.
We are a recruitment / Headhunting Consultancy so some visitors may want to apply for positions through loading their CV / Details through the site.
We want to be about friendly but expertise. Honest and trustworthy with a heavy emphasis on Consultancy!

Target Market(s)

IT and Finance Job Seekers. Our clients are in the Marketing Communications sectors so needs to be appealing to that market

Industry/Entity Type

Business Consultant

Number of Pages Required

3 page

Requirements
Must have
• Our Logo as a central theme - see uploaded files
Nice to have
• Simple. Easy to use, inviting

```html
<!DOCTYPE html>
<html lang="en">
<head>
<meta charset="utf-8">
<title>Ledgerline Recruitment</title>
<link href="https://fonts.googleapis.com/css2?family=Open+Sans:wght@400;600;700&display=swap" rel="stylesheet">
<style>
:root{
  --blue:#1a9be0;
  --blue-deep:#0a85d6;
  --teal:#3cb4a7;
  --ink:#2b2b2b;
  --text:#555;
  --muted:#777;
  --dark:#3d3d3d;
  --darker:#2f2f2f;
  --footer:#3a3a3a;
  --footer-bar:#2a2a2a;
  --ring:#1a5fa8;
  --ring-light:#ddd;
  --white:#fff;
}
*{box-sizing:border-box;margin:0;padding:0}
html,body{width:1200px;height:2889px;overflow:hidden}
body{font-family:"Open Sans",Arial,sans-serif;color:var(--text);background:var(--white);position:relative}
.abs{position:absolute}

/* hero */
.hero{position:absolute;left:0;top:0;width:1200px;height:591px;
  background:linear-gradient(100deg,#2a2e35 0%,#4a5260 18%,#8a98a8 40%,#c4ccd4 62%,#9aa6b2 82%,#6c7684 100%)}
.brand{position:absolute;left:96px;top:30px;color:var(--white);font-weight:700;font-size:38px;letter-spacing:-1px;line-height:1}
.brand small{display:block;font-size:15px;font-weight:400;letter-spacing:9px;margin-top:4px}
.nav{position:absolute;top:57px;right:108px;display:flex;gap:48px;font-size:11px;font-weight:600;color:#222;text-transform:uppercase}
.nav .active{color:var(--blue)}
.hero-copy{position:absolute;right:96px;top:255px;text-align:right;color:var(--white)}
.hero-copy h1{font-size:31px;font-weight:600;letter-spacing:.5px}
.hero-copy p{font-size:22px;margin-top:14px}
.hero-btns{display:flex;gap:14px;justify-content:flex-end;margin-top:22px}
.btn{display:inline-block;font-size:18px;font-weight:600;color:var(--white);padding:9px 20px}
.btn-dark{background:#333}
.btn-blue{background:var(--blue)}
.arrow{position:absolute;top:300px}

/* section heads */
.sec-title{position:absolute;left:0;width:1200px;text-align:center;font-size:25px;font-weight:600;color:var(--ink)}
.rule{position:absolute;left:515px;width:170px;height:3px;background:var(--blue)}
.lead{position:absolute;left:140px;width:920px;text-align:center;font-size:12.5px;line-height:26px;color:var(--text)}

/* stats */
.stat{position:absolute;top:853px;width:148px;height:148px;text-align:center}
.stat svg{position:absolute;left:0;top:0}
.stat .num{position:absolute;left:0;right:0;top:42px;font-size:24px;color:var(--ink)}
.stat .lbl{position:absolute;left:10px;right:10px;top:82px;font-size:12px;font-weight:600;color:var(--ink);line-height:19px}

/* audience boxes */
.aud{position:absolute;top:1065px;width:485px;height:229px;border-radius:4px;color:var(--white);padding:28px 37px}
.aud.employers{left:98px;background:linear-gradient(180deg,#18a8ea,#0a86d8)}
.aud.candidates{left:617px;background:linear-gradient(180deg,#5ec3b8,#33a99c)}
.aud h3{font-size:22px;font-weight:600;display:flex;align-items:center;gap:14px}
.aud p{font-size:11.5px;line-height:23px;margin-top:18px}
.aud .reg{display:inline-block;margin-top:18px;border:1px solid var(--white);padding:8px 23px;font-size:16px;font-weight:600}

/* featured */
.featured{position:absolute;left:0;top:1362px;width:1200px;height:287px;background:linear-gradient(180deg,var(--dark),var(--darker))}
.featured .sec-title{color:var(--white);top:48px}
.featured .rule{top:94px;background:var(--white)}
.partners{position:absolute;top:168px;left:96px;width:1008px;display:flex}
.partner{flex:1;text-align:center;color:var(--white);font-size:30px;font-weight:600;border-right:1px solid #666;display:flex;align-items:center;justify-content:center;gap:10px;height:58px}
.partner:last-child{border-right:none}
.partner .dot{width:16px;height:16px;border:1.5px solid var(--white);border-radius:50%}

/* news */
.card{position:absolute;top:1880px;width:306px;text-align:center}
.card .ph{width:306px;height:152px;border:3px solid #e4e4e4}
.card .meta{margin-top:18px;font-size:12px;color:var(--blue)}
.card .date{margin-top:12px;font-size:12px;color:var(--blue);display:flex;gap:8px;justify-content:center;align-items:center}
.card h4{margin-top:16px;font-size:13.5px;font-weight:600;color:var(--ink);line-height:21px}
.card p{margin-top:10px;font-size:11.5px;line-height:21px;color:var(--text)}

/* map */
.map{position:absolute;left:0;top:2284px;width:1200px;height:283px;background:linear-gradient(135deg,#b9c3a8,#d8d2bf 45%,#c5cbd0)}

/* footer */
.footer{position:absolute;left:0;top:2567px;width:1200px;height:249px;background:var(--footer);color:var(--white)}
.foot-brand{position:absolute;left:96px;top:88px;font-size:30px;font-weight:700;letter-spacing:-1px;line-height:1}
.foot-brand small{display:block;font-size:12px;font-weight:400;letter-spacing:7px;margin-top:4px}
.col{position:absolute;top:46px}
.col h5{font-size:15px;font-weight:600;margin-bottom:14px}
.col li{list-style:none;font-size:12px;line-height:27.5px}
.col li::before{content:"»";margin-right:12px}
.contact-row{display:flex;gap:16px;font-size:11.5px;line-height:21px;margin-bottom:14px}
.social{display:flex;gap:12px;margin-top:4px}
.social span{width:34px;height:34px;border:2px solid var(--white);border-radius:50%}
.bottom{position:absolute;left:0;top:2816px;width:1200px;height:73px;background:var(--footer-bar);color:var(--white);font-size:12px;text-align:center;line-height:73px}
</style>
</head>
<body>

<section class="hero" role="img" aria-label="Photo of a recruiter interviewing a candidate across a desk in a bright office">
</section>
<div class="brand">Ledgerline<small>Recruitment</small></div>
<nav class="nav"><span class="active">Home</span><span>About us</span><span>Services</span><span>Recruitment rate</span><span>Blog</span><span>Contact us</span></nav>
<svg class="arrow" style="left:50px" width="14" height="24" viewBox="0 0 14 24"><path d="M12 2 2 12l10 10" fill="none" stroke="#fff" stroke-width="2.5"/></svg>
<svg class="arrow" style="right:50px" width="14" height="24" viewBox="0 0 14 24"><path d="M2 2l10 10-10 10" fill="none" stroke="#fff" stroke-width="2.5"/></svg>
<div class="hero-copy">
  <h1>LEDGERLINE RECRUITMENT</h1>
  <p>We are Headhunters and Recruitment</p>
  <div class="hero-btns"><span class="btn btn-dark">Sign In</span><span class="btn btn-blue">Know More Info</span></div>
</div>

<h2 class="sec-title" style="top:634px">WELCOME TO LEDGERLINE RECRUITMENT</h2>
<div class="rule" style="top:690px"></div>
<p class="lead" style="top:726px">Posse verterem recteque at sea. Deserunt scribentur vim et, sed ne diam dolorum propriae, omnium aliquam honestatis id qui. Cum at eleifend posidonium, vel et molestie tacimates, vidit facete sadipscing usu et. Quem aeterno molestie has cu, vim ne quis graeci democritum. Eam viderer reprehendunt an. No sumo elit forensibus lus, no pertinax assentior per, eu case nominati cum. vim ne quis graeci democritum.vim ne quis graeci democritum.</p>

<div class="stat" style="left:169px">
  <svg width="148" height="148" viewBox="0 0 148 148"><circle cx="74" cy="74" r="70" fill="none" stroke="var(--ring-light)" stroke-width="4"/><circle cx="74" cy="74" r="70" fill="none" stroke="var(--ring)" stroke-width="4" stroke-dasharray="374 440" transform="rotate(-90 74 74)"/></svg>
  <div class="num">85%</div><div class="lbl">JOB SEEKERS</div>
</div>
<div class="stat" style="left:409px">
  <svg width="148" height="148" viewBox="0 0 148 148"><circle cx="74" cy="74" r="70" fill="none" stroke="var(--ring-light)" stroke-width="4"/><circle cx="74" cy="74" r="70" fill="none" stroke="#2f86c8" stroke-width="4" stroke-dasharray="286 440" transform="rotate(-90 74 74)"/></svg>
  <div class="num">65%</div><div class="lbl">RECRUITEMENT DONE</div>
</div>
<div class="stat" style="left:648px">
  <svg width="148" height="148" viewBox="0 0 148 148"><circle cx="74" cy="74" r="70" fill="none" stroke="var(--ring-light)" stroke-width="4"/><circle cx="74" cy="74" r="70" fill="none" stroke="#6fb2e0" stroke-width="4" stroke-dasharray="242 440" transform="rotate(-90 74 74)"/></svg>
  <div class="num">55%</div><div class="lbl">RECRUITERS</div>
</div>
<div class="stat" style="left:872px">
  <svg width="148" height="148" viewBox="0 0 148 148"><circle cx="74" cy="74" r="70" fill="none" stroke="var(--ring-light)" stroke-width="4"/><circle cx="74" cy="74" r="70" fill="none" stroke="var(--ring)" stroke-width="4" stroke-dasharray="330 440" transform="rotate(-90 74 74)"/></svg>
  <div class="num">75%</div><div class="lbl">SATISFIED PLACEMENT</div>
</div>

<div class="aud employers">
  <h3><svg width="22" height="22" viewBox="0 0 22 22"><circle cx="8.5" cy="8.5" r="6" fill="none" stroke="#fff" stroke-width="3"/><path d="M13 13l7 7" stroke="#fff" stroke-width="4"/></svg>EMPLOYERS</h3>
  <p>No nisl quidam vim, mei in oratio mentitum torquatos, his elit zril ut. Pro no amet nullam, vim audiam voluptua ei . No nisl quidam vim, mei in oratio mentitum torquatos, his elit zril ut. Pro no amet nullam.</p>
  <span class="reg">Register yourself</span>
</div>
<div class="aud candidates">
  <h3><svg width="22" height="22" viewBox="0 0 22 22"><rect x="1" y="9" width="20" height="12" fill="#fff"/><circle cx="8" cy="5" r="4" fill="#fff"/></svg>CANDIDATES</h3>
  <p>No nisl quidam vim, mei in oratio mentitum torquatos, his elit zril ut. Pro no amet nullam, vim audiam voluptua ei . No nisl quidam vim, mei in oratio mentitum torquatos, his elit zril ut. Pro no amet nullam.</p>
  <span class="reg">Register yourself</span>
</div>

<section class="featured">
  <h2 class="sec-title">FEATURED COMPANIES</h2>
  <div class="rule"></div>
  <svg class="abs" style="left:30px;top:136px" width="10" height="18" viewBox="0 0 10 18"><path d="M9 1 1 9l8 8" fill="none" stroke="#aaa" stroke-width="2"/></svg>
  <svg class="abs" style="right:30px;top:136px" width="10" height="18" viewBox="0 0 10 18"><path d="M1 1l8 8-8 8" fill="none" stroke="#aaa" stroke-width="2"/></svg>
  <div class="partners">
    <div class="partner">Norvane<span class="dot"></span></div>
    <div class="partner">Kestrel Capital</div>
    <div class="partner">Brightfield Energy</div>
    <div class="partner">Glad Partner</div>
  </div>
</section>

<h2 class="sec-title" style="top:1699px">RECENT NEWS</h2>
<div class="rule" style="top:1756px"></div>
<p class="lead" style="top:1792px">Posse verterem recteque at sea. Deserunt scribentur vim et, sed ne diam dolorum propriae, omnium aliquam honestatis id qui. Cum at eleifend posidonium, vel et molestie tacimates, vidit facete sadipscing usu et. Quem aeterno molestie has cu, vim ne quis graeci democritum. Eam viderer reprehendunt an.</p>

<article class="card" style="left:100px">
  <div class="ph" role="img" aria-label="Photo of business people shaking hands across a meeting table" style="background:linear-gradient(180deg,#9fb4c8,#5d6b7a)"></div>
  <div class="meta">Lorem Ipsum &nbsp;•&nbsp; Ei apiriaen</div>
  <div class="date"><svg width="12" height="12" viewBox="0 0 12 12"><rect x="1" y="2" width="10" height="9" fill="none" stroke="#555" stroke-width="1.5"/><path d="M1 5h10" stroke="#555"/></svg>10 months ago</div>
  <h4>Vel ne appetere iudicab accusamus soluta repudiare esseapp</h4>
  <p>An latine iracundia vix. Mei antiopam praesent et, is nam et malis sapientem. In solum omnium voluptaria vim, natum civibus delicata antiopam</p>
</article>
<article class="card" style="left:448px">
  <div class="ph" role="img" aria-label="Photo of a smiling businessman working at a laptop" style="background:linear-gradient(180deg,#c9d4dc,#7d8790)"></div>
  <div class="meta">Lorem Ipsum &nbsp;•&nbsp; Ei apiriaen</div>
  <div class="date"><svg width="12" height="12" viewBox="0 0 12 12"><rect x="1" y="2" width="10" height="9" fill="none" stroke="#555" stroke-width="1.5"/><path d="M1 5h10" stroke="#555"/></svg>10 months ago</div>
  <h4>Vel ne appetere iudicab accusamus soluta repudiare esseapp</h4>
  <p>An latine iracundia vix. Mei antiopam praesent et, is nam et malis sapientem. In solum omnium voluptaria vim, natum civibus delicata antiopam</p>
</article>
<article class="card" style="left:794px">
  <div class="ph" role="img" aria-label="Photo of a job interview with a panel of interviewers" style="background:linear-gradient(180deg,#e2e0da,#8a8680)"></div>
  <div class="meta">Lorem Ipsum &nbsp;•&nbsp; Ei apiriaen</div>
  <div class="date"><svg width="12" height="12" viewBox="0 0 12 12"><rect x="1" y="2" width="10" height="9" fill="none" stroke="#555" stroke-width="1.5"/><path d="M1 5h10" stroke="#555"/></svg>10 months ago</div>
  <h4>Vel ne appetere iudicab accusamus soluta repudiare esseapp</h4>
  <p>An latine iracundia vix. Mei antiopam praesent et, is nam et malis sapientem. In solum omnium voluptaria vim, natum civibus delicata antiopam</p>
</article>

<div class="map" role="img" aria-label="Street map of the city centre with a location pin marking the office"></div>

<footer class="footer">
  <div class="foot-brand">Ledgerline<small>Recruitment</small></div>
  <div class="col" style="left:337px"><h5>MENUS</h5><ul><li>Home</li><li>About us</li><li>Our services</li><li>Blog</li><li>Contact us</li></ul></div>
  <div class="col" style="left:485px"><h5>QUICK LINKS</h5><ul><li>Site map</li><li>Terms and Conditions</li><li>Disclaimer</li><li>Privacy Policy</li><li>Contact us</li></ul></div>
  <div class="col" style="left:682px;width:200px"><h5 style="margin-bottom:18px">CONTACT US</h5>
    <div class="contact-row"><svg width="16" height="14" viewBox="0 0 16 14"><path d="M8 0 0 7h2v7h4V9h4v5h4V7h2z" fill="#fff"/></svg><span>220 Harbour Row | Eastfield<br>KS 60210</span></div>
    <div class="contact-row"><svg width="16" height="16" viewBox="0 0 16 16"><rect x="4" y="0" width="8" height="16" rx="1.5" fill="none" stroke="#fff" stroke-width="1.5"/></svg><span>Call Us : (555)010-2048</span></div>
    <div class="contact-row"><svg width="16" height="12" viewBox="0 0 16 12"><rect x="1" y="1" width="14" height="10" fill="none" stroke="#fff" stroke-width="1.5"/><path d="M1 1l7 6 7-6" fill="none" stroke="#fff" stroke-width="1.5"/></svg><span>info@ledgerline.example</span></div>
  </div>
  <div class="col" style="left:922px"><h5 style="margin-bottom:20px">CONNECT US WITH</h5><div class="social"><span></span><span></span><span></span><span></span></div></div>
</footer>
<div class="bottom">© &nbsp;Companyname 2016 . All Rights Reserved</div>

</body>
</html>
```